Relaunch configurator for lighting

We just need a new modern design for our configurator
http://lichtkonfigurator.vemtra.at

Design must be responsive

Number of Pages Required

1 page

```html
<!DOCTYPE html>
<html lang="en">
<head>
<meta charset="utf-8">
<title>Lumora Light Studio – Configurator</title>
<link rel="stylesheet" href="https://fonts.googleapis.com/css2?family=Poppins:wght@300;400;500;600&display=swap">
<style>
  :root {
    --page-bg: #e3e5ea;
    --white: #ffffff;
    --ink: #1b1b1b;
    --accent: #8e1010;
    --muted: #8a8a8a;
    --line: #d6d6d6;
    --night-blue: #0d2a6a;
    --sky-top: #3e3fb0;
    --sky-mid: #2a3c9a;
    --dusk: #c3602f;
  }
  * { box-sizing: border-box; margin: 0; padding: 0; }
  html, body {
    width: 1200px; height: 750px; overflow: hidden;
    background: var(--page-bg);
    font-family: "Poppins", sans-serif;
  }
  .stage {
    position: absolute; left: 58px; top: 52px;
    width: 1079px; height: 654px;
    border-radius: 4px; overflow: hidden;
  }
  .hero-right {
    position: absolute; left: 428px; top: 0; right: 0; bottom: 0;
    background: linear-gradient(180deg, var(--sky-top) 0%, var(--sky-mid) 40%, #3a2f7a 62%, #7a3e4a 80%, var(--dusk) 100%);
  }
  .hero-left {
    position: absolute; left: 0; top: 0; width: 428px; bottom: 0;
    background:
      radial-gradient(circle at 48% 58%, #5f8eea 0%, #2d58b8 28%, #10265a 55%, #060d20 100%);
  }
  .brand {
    position: absolute; left: 44px; top: 116px;
    display: flex; align-items: center; gap: 12px;
  }
  .brand-mark { width: 18px; height: 18px; background: var(--white); }
  .brand-name {
    font-weight: 600; font-size: 30px; color: var(--white);
    letter-spacing: 0.5px; white-space: nowrap;
  }
  .copyright {
    position: absolute; left: 91px; top: 604px;
    font-size: 10.5px; color: var(--white);
  }
  .tagline {
    position: absolute; right: 50px; top: 81px;
    text-align: right; color: var(--white);
    font-size: 17px; font-weight: 300; line-height: 30px;
  }
  .cards {
    position: absolute; left: 367px; top: 229px;
    display: flex; gap: 22.5px;
  }
  .card {
    position: relative; width: 205.5px; height: 266px;
    background: var(--white); border-radius: 4px;
    box-shadow: 0 4px 14px rgba(0,0,0,0.18);
  }
  .card-icon {
    position: absolute; left: 50%; top: 24px; transform: translateX(-50%);
    width: 66px; height: 66px;
  }
  .card-icon svg { width: 100%; height: 100%; }
  .strip-photo {
    position: absolute; left: 166px; top: 0; width: 30px; height: 46px;
    background: linear-gradient(180deg, #f4efe2, #e0c98a 50%, #f2ede0);
    box-shadow: 0 1px 3px rgba(0,0,0,0.25);
  }
  .card-title {
    position: absolute; left: 0; right: 0; top: 98px;
    text-align: center; font-weight: 600; font-size: 11.5px;
    line-height: 14.5px; color: var(--ink);
  }
  .range-bar {
    position: absolute; left: 22.5px; top: 146px;
    width: 158px; height: 40.5px;
    display: flex; align-items: center; justify-content: center;
    color: var(--white); font-size: 13.5px; font-weight: 300;
  }
  .range-bar.duo { background: linear-gradient(90deg, #eebf7b, #a4bed2); }
  .range-bar.rgb { background: linear-gradient(90deg, #e51212 0%, #8d5a2a 30%, #11a23a 55%, #0f6ad0 100%); }
  .config-input {
    position: absolute; left: 24px; top: 146px;
    width: 158px; height: 40.5px;
    border: 1px solid var(--line); padding: 0 11px;
    font-family: "Poppins", sans-serif; font-size: 9.5px; color: var(--muted);
    background: var(--white);
  }
  .config-input::placeholder { color: var(--muted); }
  .card-links {
    position: absolute; left: 0; right: 0; top: 217px;
    display: flex; justify-content: center; align-items: center;
  }
  .card-links a {
    color: var(--accent); font-size: 10px; font-weight: 500;
    text-decoration: none; padding: 0 0; text-align: center;
  }
  .card-links .sep { width: 1px; height: 22.5px; background: var(--line); }
  .card-links.ranges a { width: 70px; }
  .card-links.actions a:first-child { width: 68px; }
  .card-links.actions a:last-child { width: 120px; }
</style>
</head>
<body>
  <main class="stage">
    <div class="hero-right" role="img" aria-label="Modern building with blue-lit glass roof against a dusk sky"></div>
    <div class="hero-left" role="img" aria-label="Close-up of a glowing blue LED spotlight bulb"></div>

    <div class="brand">
      <span class="brand-mark"></span>
      <span class="brand-name">Lumora Light Studio</span>
    </div>
    <p class="copyright">Copyright © 2020 Lumora Light Studio.</p>

    <p class="tagline">Individual and stepless setting of the light<br>color from cold white to warm white.</p>

    <section class="cards">
      <article class="card">
        <div class="strip-photo" role="img" aria-label="Dual-white LED strip segment"></div>
        <div class="card-icon">
          <svg viewBox="0 0 66 66" fill="none" stroke="#8e1010" stroke-width="2.6">
            <rect x="12" y="17" width="32" height="42" rx="4"/>
            <path d="M22 17V12a4 4 0 0 1 4-4h24a4 4 0 0 1 4 4v34a4 4 0 0 1-4 4h-6"/>
          </svg>
        </div>
        <h2 class="card-title">Create a new DUO<br>configuration</h2>
        <div class="range-bar duo">2700 K – 6000 K</div>
        <nav class="card-links ranges"><a href="#">1 - 12</a><span class="sep"></span><a href="#">13 - 24</a></nav>
      </article>

      <article class="card">
        <div class="strip-photo" role="img" aria-label="RGB LED strip segment"></div>
        <div class="card-icon">
          <svg viewBox="0 0 66 66" fill="none" stroke="#8e1010" stroke-width="2.6">
            <circle cx="33" cy="24" r="15"/>
            <circle cx="24" cy="40" r="15"/>
            <circle cx="42" cy="40" r="15"/>
          </svg>
        </div>
        <h2 class="card-title">Create a new RGB<br>configuration</h2>
        <div class="range-bar rgb"></div>
        <nav class="card-links ranges"><a href="#">1 - 12</a><span class="sep"></span><a href="#">13 - 24</a></nav>
      </article>

      <article class="card">
        <div class="card-icon">
          <svg viewBox="-1 -1 26 26" fill="none" stroke="#8e1010" stroke-width="1.1" stroke-linejoin="round">
            <circle cx="12" cy="12" r="3"/>
            <path d="M19.4 15a1.65 1.65 0 0 0 .33 1.82l.06.06a2 2 0 0 1 0 2.83 2 2 0 0 1-2.83 0l-.06-.06a1.65 1.65 0 0 0-1.82-.33 1.65 1.65 0 0 0-1 1.51V21a2 2 0 0 1-2 2 2 2 0 0 1-2-2v-.09A1.65 1.65 0 0 0 9 19.4a1.65 1.65 0 0 0-1.82.33l-.06.06a2 2 0 0 1-2.83 0 2 2 0 0 1 0-2.83l.06-.06a1.65 1.65 0 0 0 .33-1.82 1.65 1.65 0 0 0-1.51-1H3a2 2 0 0 1-2-2 2 2 0 0 1 2-2h.09A1.65 1.65 0 0 0 4.6 9a1.65 1.65 0 0 0-.33-1.82l-.06-.06a2 2 0 0 1 0-2.83 2 2 0 0 1 2.83 0l.06.06a1.65 1.65 0 0 0 1.82.33H9a1.65 1.65 0 0 0 1-1.51V3a2 2 0 0 1 2-2 2 2 0 0 1 2 2v.09a1.65 1.65 0 0 0 1 1.51 1.65 1.65 0 0 0 1.82-.33l.06-.06a2 2 0 0 1 2.83 0 2 2 0 0 1 0 2.83l-.06.06a1.65 1.65 0 0 0-.33 1.82V9a1.65 1.65 0 0 0 1.51 1H21a2 2 0 0 1 2 2 2 2 0 0 1-2 2h-.09a1.65 1.65 0 0 0-1.51 1z"/>
          </svg>
        </div>
        <h2 class="card-title">Load and edit the<br>existing configuration</h2>
        <input class="config-input" type="text" placeholder="Configuration Number">
        <nav class="card-links actions"><a href="#">Laden</a><span class="sep"></span><a href="#">PDF herunterladen</a></nav>
      </article>
    </section>
  </main>
</body>
</html>
```